Velgrijder

2 homepage design for my tire webshop. One for the winter and one for the summer.
2 items have to come back.
1 a filterbox option to choose tire width, height and inch
2 an option where i can sell my tire mounting service
The customer can buy tires from me but also have the option to use only my skills for mounting their own tire.
My sellingpoint is my mobile service, a webshop with his own mechanic, and my good reputation.

```html
<!DOCTYPE html>
<html lang="en">
<head>
<meta charset="utf-8">
<title>Velgrijder — Winter &amp; Summer Homepages</title>
<link href="https://fonts.googleapis.com/css2?family=Poppins:wght@400;500;600;700;800;900&display=swap" rel="stylesheet">
<style>
:root{
  --red:#e42a0c;
  --red-deep:#b8200a;
  --ink:#1b1b1b;
  --ink-2:#242424;
  --ink-3:#2e2e2e;
  --board:#a8a8a8;
  --light:#ececec;
  --light-2:#cfcfcf;
  --white:#ffffff;
  --muted:#9a9a9a;
  --text-dark:#222222;
}
*{box-sizing:border-box;margin:0;padding:0}
html,body{width:1200px;height:3967px;overflow:hidden}
body{font-family:"Poppins",sans-serif;background:var(--board);color:var(--white)}
.board{position:relative;width:1200px;height:3967px;overflow:hidden;background:var(--board)}
.abs{position:absolute}
.photo{position:absolute}

.board-head{position:absolute;left:0;top:0;width:1200px;height:607px;background:linear-gradient(180deg,#2f2f2f,#262626)}
.board-brand{position:absolute;left:0;top:82px;width:1200px;text-align:center;font-weight:800;font-size:46px;letter-spacing:2px;color:var(--white)}
.board-brand .dot{display:inline-block;width:14px;height:14px;border-radius:50%;background:var(--red);margin-right:12px;vertical-align:middle}
.board-sub{position:absolute;left:0;top:190px;width:1200px;text-align:center;font-size:24px;letter-spacing:18px;font-weight:500;color:var(--white)}
.board-label{position:absolute;top:896px;font-size:13px;letter-spacing:8px;color:#2a2a2a;font-weight:500}

.logo{position:absolute;font-weight:800;color:var(--white);letter-spacing:.5px}
.btn{position:absolute;background:var(--red);color:var(--white);font-weight:600;display:flex;align-items:center;justify-content:center;gap:4px;white-space:nowrap}
.btn-dark{background:#5a1a10;color:#e0836f}
.nav{position:absolute;display:flex;color:#d9d9d9;white-space:nowrap}
.nav span.on{color:var(--white);font-weight:600}
.eyebrow{position:absolute;letter-spacing:6px;color:var(--white);font-weight:500}
.display{position:absolute;font-weight:900;line-height:.95;text-transform:uppercase}
.display .r{color:var(--red)}
.para{position:absolute;color:#bdbdbd;line-height:1.55}
.para.dark{color:#555}
.h2{position:absolute;font-weight:800;line-height:1.1}
.h2.dark{color:var(--text-dark)}
.rule{position:absolute;height:1px;background:var(--red)}
.bullets{position:absolute;list-style:none}
.bullets li{display:flex;align-items:flex-start;color:#cfcfcf}
.bullets .ic{flex:none;border-radius:50%;border:2px solid var(--red);background:linear-gradient(90deg,var(--red) 50%,transparent 50%)}
.select{position:absolute;background:var(--white);border:1px solid #d4d4d4;color:#b5b5b5;display:flex;align-items:center;justify-content:space-between}
.select::after{content:"";width:4px;height:4px;border-right:1.5px solid #333;border-bottom:1.5px solid #333;transform:rotate(45deg);margin-top:-2px}
.flabel{position:absolute;font-weight:700;color:var(--text-dark);display:flex;align-items:center;gap:8px}
.flabel::after{content:"";width:40px;height:1px;background:var(--red)}
.feature{position:absolute;display:flex;align-items:center;color:var(--white);font-weight:600;line-height:1.3}
.feature .fi{flex:none;border-radius:50%;background:rgba(0,0,0,.22);display:flex;align-items:center;justify-content:center}
.card{position:absolute;overflow:hidden}
.card .img{position:absolute;left:0;top:0;width:100%;background:linear-gradient(180deg,#2b2b2b,#3a3a3a);}
.card .tag{position:absolute;color:#ddd}
.card .tyre{position:absolute;border-radius:50%;background:radial-gradient(circle,#8d8d8d 0 28%,#1a1a1a 30% 62%,#0e0e0e 64%)}
.card .name{position:absolute;font-weight:600;color:var(--white);line-height:1.35}
.card .price{position:absolute;color:var(--red);font-weight:600}
.links{position:absolute;list-style:none;color:#bdbdbd}
.social{position:absolute;display:flex}
.social span{border-radius:50%;display:block}
.input{position:absolute;background:var(--white);color:#aaa;display:flex;align-items:center;justify-content:space-between}
</style>
</head>
<body>
<div class="board">

  <header class="board-head">
    <div class="board-brand"><span class="dot"></span>Velgrijder</div>
    <div class="board-sub">WINTER TYRES</div>
  </header>

  <!-- summer homepage hero -->
  <section class="abs summer" style="left:246px;top:342px;width:709px;height:428px;background:var(--ink);overflow:hidden">
    <div class="abs" style="left:0;top:0;width:709px;height:20px;background:var(--ink-3)"></div>
    <svg class="abs" style="left:74px;top:6px" width="8" height="8" viewBox="0 0 10 10"><circle cx="4" cy="4" r="3" fill="none" stroke="#ccc" stroke-width="1.3"/><path d="M6.5 6.5L9 9" stroke="#ccc" stroke-width="1.3"/></svg>
    <div class="abs" style="left:88px;top:5px;font-size:7px;color:#ccc">Search...</div>
    <div class="btn" style="left:459px;top:0;width:85px;height:20px;font-size:6px">Summer Tires →</div>
    <div class="btn btn-dark" style="left:551px;top:0;width:65px;height:20px;font-size:6px">Winter Tires</div>
    <div class="logo" style="left:77px;top:42px;font-size:17px">Velgrijder</div>
    <div class="nav" style="left:216px;top:47px;gap:15px;font-size:6.5px">
      <span class="on">Home</span><span>About us</span><span>Shop</span><span>Brands</span><span>Mounting &amp; Repairs</span><span>Team</span><span>Blogs</span><span>Contact us</span>
    </div>
    <div class="abs" style="left:227px;top:87px;width:5px;height:5px;border-radius:50%;background:var(--red)"></div>
    <div class="photo" role="img" aria-label="Two summer tyres on alloy rims" style="left:330px;top:120px;width:379px;height:308px;background:radial-gradient(ellipse at 45% 60%,#5a5a5a 0,#2a2a2a 45%,var(--ink) 72%)"></div>
    <div class="eyebrow" style="left:77px;top:148px;font-size:11px">SUMMER</div>
    <div class="display" style="left:75px;top:168px;font-size:50px"><span class="r">Tires &amp;</span><br>Wheels</div>
    <p class="para" style="left:77px;top:268px;width:190px;font-size:6.5px">Lorem Ipsum is simply dummy text of the printing and typesetting industry. Lorem Ipsum has been the industry's standard dummy text ever since the 1500s, when an unknown printer took a galley.</p>
    <div class="btn btn-dark" style="left:77px;top:337px;width:85px;height:24px;font-size:6.5px">Shop Tires →</div>
  </section>

  <div class="board-label" style="left:380px">DESKTOP</div>
  <div class="board-label" style="left:958px">MOBILE</div>

  <!-- DESKTOP -->
  <main class="abs desktop" style="left:94px;top:945px;width:704px;height:2930px;background:var(--ink);overflow:hidden">
    <div class="abs" style="left:0;top:0;width:704px;height:22px;background:var(--ink-3)"></div>
    <svg class="abs" style="left:74px;top:7px" width="9" height="9" viewBox="0 0 10 10"><circle cx="4" cy="4" r="3" fill="none" stroke="#ccc" stroke-width="1.3"/><path d="M6.5 6.5L9 9" stroke="#ccc" stroke-width="1.3"/></svg>
    <div class="abs" style="left:88px;top:6px;font-size:7px;color:#ccc">Search...</div>
    <div class="btn btn-dark" style="left:468px;top:0;width:69px;height:22px;font-size:6px">Summer Tires →</div>
    <div class="btn" style="left:546px;top:0;width:85px;height:22px;font-size:6px">Winter Tires →</div>

    <div class="logo" style="left:74px;top:40px;font-size:18px">Velgrijder</div>
    <div class="nav" style="left:214px;top:47px;gap:19px;font-size:7px">
      <span class="on">Home</span><span>About us</span><span>Shop</span><span>Brands</span><span>Mounting &amp; Repairs</span><span>Team</span><span>Blogs</span><span>Contact us</span>
    </div>
    <svg class="abs" style="left:610px;top:44px" width="14" height="13" viewBox="0 0 14 13"><path d="M1 2h2l2 7h7l1-5H4" fill="none" stroke="#fff" stroke-width="1.2"/><circle cx="6" cy="11" r="1" fill="#fff"/><circle cx="11" cy="11" r="1" fill="#fff"/><circle cx="12" cy="2" r="2" fill="var(--red)"/></svg>
    <div class="abs" style="left:222px;top:76px;width:5px;height:5px;border-radius:50%;background:var(--red)"></div>

    <div class="photo" role="img" aria-label="Blue car with a winter tyre on a snowy road" style="left:270px;top:82px;width:434px;height:348px;background:linear-gradient(115deg,var(--ink) 0%,#2f4a5e 30%,#2a6f95 45%,#3a3a3a 60%,#1c1c1c 100%)"></div>
    <div class="photo" aria-hidden="true" style="left:0;top:82px;width:330px;height:348px;background:linear-gradient(180deg,#3a3a3a,var(--ink) 45%)"></div>
    <div class="eyebrow" style="left:74px;top:176px;font-size:11px">OUR</div>
    <div class="display" style="left:72px;top:195px;font-size:52px"><span class="r">Winter</span><br>Tires</div>
    <div class="btn btn-dark" style="left:74px;top:308px;width:88px;height:25px;font-size:6.5px">Shop Tires →</div>

    <section class="abs" style="left:74px;top:430px;width:556px;height:252px;background:linear-gradient(180deg,#f4f4f4,#c8c8c8)">
      <div class="h2 dark" style="left:34px;top:30px;font-size:13px;font-weight:700">Find Wheels &amp; Tires That Fit</div>
      <p class="para dark" style="left:34px;top:58px;width:440px;font-size:6.5px">Lorem Ipsum is simply dummy text of the printing and typesetting industry. Lorem Ipsum has been the industry's standard dummy text ever since the 1500s, when an unknown printer took a galley.</p>
      <svg class="abs" style="left:505px;top:62px" width="12" height="12" viewBox="0 0 12 12"><path d="M10 6a4 4 0 1 1-1.2-2.8" fill="none" stroke="#333" stroke-width="1.2"/><path d="M9 1v2.5H6.5" fill="none" stroke="#333" stroke-width="1.2"/></svg>
      <div class="flabel" style="left:34px;top:94px;font-size:6.5px">BY SIZE</div>
      <div class="select" style="left:34px;top:108px;width:152px;height:22px;font-size:6px;padding:0 8px">Width</div>
      <div class="select" style="left:201px;top:108px;width:152px;height:22px;font-size:6px;padding:0 8px">Height</div>
      <div class="select" style="left:368px;top:108px;width:152px;height:22px;font-size:6px;padding:0 8px">Inch</div>
      <div class="flabel" style="left:34px;top:138px;font-size:6.5px">BY VEHICLE</div>
      <div class="flabel" style="left:201px;top:138px;font-size:6.5px">BRAND</div>
      <div class="flabel" style="left:368px;top:138px;font-size:6.5px">TYPE</div>
      <div class="select" style="left:34px;top:152px;width:152px;height:22px;font-size:6px;padding:0 8px">Model</div>
      <div class="select" style="left:201px;top:152px;width:152px;height:22px;font-size:6px;padding:0 8px">Select</div>
      <div class="select" style="left:368px;top:152px;width:152px;height:22px;font-size:6px;padding:0 8px">Select</div>
      <div class="btn" style="left:34px;top:193px;width:487px;height:24px;font-size:7px">Search →</div>
    </section>
    <div class="abs" style="left:352px;top:684px;width:0;height:34px;border-left:1px dashed #666"></div>

    <div class="photo" role="img" aria-label="Close-up of a winter tyre tread" style="left:0;top:733px;width:353px;height:300px;background:radial-gradient(ellipse at 60% 40%,#5c5c5c 0,#3a3a3a 40%,#1c1c1c 80%)"></div>
    <div class="h2" style="left:406px;top:750px;font-size:19px">How Our Winter<br>Tires Work</div>
    <div class="rule" style="left:583px;top:761px;width:47px"></div>
    <p class="para" style="left:406px;top:805px;width:222px;font-size:6.5px">Lorem Ipsum is simply dummy text of the printing and typesetting industry. Lorem Ipsum has been the industry's standard dummy text ever since the 1500s, when an unknown printer took a galley.</p>
    <ul class="bullets" style="left:406px;top:872px;width:222px;font-size:7px">
      <li style="gap:12px;margin-bottom:14px"><span class="ic" style="width:12px;height:12px"></span>Compound remains flexible in cold weather.</li>
      <li style="gap:12px;margin-bottom:14px"><span class="ic" style="width:12px;height:12px"></span>Tread designed for traction in ice, slush and snow.</li>
      <li style="gap:12px;margin-bottom:14px"><span class="ic" style="width:12px;height:12px"></span>More sipes give thousands of biting edge.</li>
      <li style="gap:12px"><span class="ic" style="width:12px;height:12px"></span>Stud holes</li>
    </ul>

    <section class="abs" style="left:0;top:1033px;width:704px;height:351px;background:var(--light)">
      <div class="photo" role="img" aria-label="Car wheel driving through a snowy forest" style="left:260px;top:0;width:444px;height:351px;background:linear-gradient(90deg,var(--light) 0%,#dcdfe3 30%,#b9bec4 65%,#8e949a 100%)"></div>
      <div class="h2 dark" style="left:74px;top:58px;font-size:19px">More About Our<br>Winter Tires</div>
      <div class="rule" style="left:250px;top:69px;width:46px"></div>
      <p class="para dark" style="left:74px;top:118px;width:225px;font-size:6.3px">Lorem Ipsum is simply dummy text of the printing and typesetting industry. Lorem Ipsum has been the industry's standard dummy text ever since the 1500s, when an unknown printer took a galley of type and scrambled it to make a type specimen book. It has survived not only five centuries, but also the leap into electronic typesetting, remaining essentially unchanged. It was popularised in the 1960s with the release of Plintor sheets containing Lorem Ipsum passages, and more recently with desktop publishing software like Kerndale Layout including versions of Lorem Ipsum.</p>
      <p class="para dark" style="left:74px;top:232px;width:225px;font-size:6.3px">Lorem Ipsum is simply dummy text of the printing and typesetting industry.</p>
      <div class="btn" style="left:74px;top:272px;width:88px;height:25px;font-size:6.5px;background:#f08a76">Shop Tires →</div>
    </section>

    <section class="abs" style="left:29px;top:1413px;width:647px;height:94px;background:linear-gradient(180deg,var(--red),var(--red-deep))">
      <div class="feature" style="left:44px;top:30px;gap:12px;font-size:7px"><span class="fi" style="width:34px;height:34px"><svg width="16" height="16" viewBox="0 0 16 16"><circle cx="8" cy="8" r="6" fill="none" stroke="#fff" stroke-width="1.5"/><circle cx="8" cy="8" r="2.5" fill="#fff"/></svg></span>State of the Art<br>Mounting</div>
      <div class="feature" style="left:198px;top:30px;gap:12px;font-size:7px"><span class="fi" style="width:34px;height:34px"><svg width="18" height="14" viewBox="0 0 18 14"><path d="M1 2h10v8H1zM11 5h4l2 3v2h-6" fill="none" stroke="#fff" stroke-width="1.3"/><circle cx="4" cy="11" r="1.6" fill="#fff"/><circle cx="14" cy="11" r="1.6" fill="#fff"/></svg></span>Fast and Hassle<br>free Shipping</div>
      <div class="feature" style="left:355px;top:30px;gap:12px;font-size:7px"><span class="fi" style="width:34px;height:34px"><svg width="16" height="16" viewBox="0 0 16 16"><circle cx="8" cy="7" r="5" fill="none" stroke="#fff" stroke-width="1.3"/><path d="M5.5 7l2 2 3-3.5M5 11l-1 4 4-2 4 2-1-4" fill="none" stroke="#fff" stroke-width="1.2"/></svg></span>100% Guaranteed<br>Fitment</div>
      <div class="feature" style="left:509px;top:30px;gap:12px;font-size:7px"><span class="fi" style="width:34px;height:34px"><svg width="16" height="16" viewBox="0 0 16 16"><circle cx="8" cy="5" r="3.5" fill="#fff"/><path d="M2 15c0-4 3-6 6-6s6 2 6 6z" fill="#fff"/></svg></span>We're Tire<br>Experts</div>
    </section>

    <div class="display" style="left:0;top:1565px;width:704px;text-align:center;font-size:40px"><span class="r">Shop</span> Now</div>
    <p class="para" style="left:148px;top:1622px;width:408px;text-align:center;font-size:6.5px">Lorem Ipsum is simply dummy text of the printing and typesetting industry. Lorem Ipsum has been the industry's standard dummy text ever since the 1500s, when an unknown printer took a galley.</p>

    <div class="card" style="left:74px;top:1683px;width:129px;height:220px"><div class="img" role="img" aria-label="Winter tyre product photo" style="height:140px"></div><div class="tyre" style="left:22px;top:26px;width:100px;height:108px"></div><span class="tag" style="left:9px;top:8px;font-size:5.5px">❄ Winter</span><div class="name" style="left:0;top:148px;width:129px;font-size:6.3px">Lorem Ipsum is simply dummy text of the printing</div><div class="price" style="left:0;top:181px;font-size:12px">$199</div></div>
    <div class="card" style="left:215px;top:1683px;width:129px;height:220px"><div class="img" role="img" aria-label="Winter tyre product photo" style="height:140px"></div><div class="tyre" style="left:22px;top:26px;width:100px;height:108px"></div><span class="tag" style="left:9px;top:8px;font-size:5.5px">❄ Winter</span><div class="name" style="left:0;top:148px;width:129px;font-size:6.3px">Lorem Ipsum is simply dummy text of the printing</div><div class="price" style="left:0;top:181px;font-size:12px">$199</div></div>
    <div class="card" style="left:358px;top:1683px;width:129px;height:220px"><div class="img" role="img" aria-label="Winter tyre product photo" style="height:140px"></div><div class="tyre" style="left:22px;top:26px;width:100px;height:108px"></div><span class="tag" style="left:9px;top:8px;font-size:5.5px">❄ Winter</span><div class="name" style="left:0;top:148px;width:129px;font-size:6.3px">Lorem Ipsum is simply dummy text of the printing</div><div class="price" style="left:0;top:181px;font-size:12px">$199</div></div>
    <div class="card" style="left:500px;top:1683px;width:129px;height:220px"><div class="img" role="img" aria-label="Winter tyre product photo" style="height:140px"></div><div class="tyre" style="left:22px;top:26px;width:100px;height:108px"></div><span class="tag" style="left:9px;top:8px;font-size:5.5px">❄ Winter</span><div class="name" style="left:0;top:148px;width:129px;font-size:6.3px">Lorem Ipsum is simply dummy text of the printing</div><div class="price" style="left:0;top:181px;font-size:12px">$199</div></div>
    <div class="card" style="left:74px;top:1953px;width:129px;height:220px"><div class="img" role="img" aria-label="Winter tyre product photo" style="height:140px"></div><div class="tyre" style="left:22px;top:26px;width:100px;height:108px"></div><span class="tag" style="left:9px;top:8px;font-size:5.5px">❄ Winter</span><div class="name" style="left:0;top:148px;width:129px;font-size:6.3px">Lorem Ipsum is simply dummy text of the printing</div><div class="price" style="left:0;top:181px;font-size:12px">$199</div></div>
    <div class="card" style="left:215px;top:1953px;width:129px;height:220px"><div class="img" role="img" aria-label="Winter tyre product photo" style="height:140px"></div><div class="tyre" style="left:22px;top:26px;width:100px;height:108px"></div><span class="tag" style="left:9px;top:8px;font-size:5.5px">❄ Winter</span><div class="name" style="left:0;top:148px;width:129px;font-size:6.3px">Lorem Ipsum is simply dummy text of the printing</div><div class="price" style="left:0;top:181px;font-size:12px">$199</div></div>
    <div class="card" style="left:358px;top:1953px;width:129px;height:220px"><div class="img" role="img" aria-label="Winter tyre product photo" style="height:140px"></div><div class="tyre" style="left:22px;top:26px;width:100px;height:108px"></div><span class="tag" style="left:9px;top:8px;font-size:5.5px">❄ Winter</span><div class="name" style="left:0;top:148px;width:129px;font-size:6.3px">Lorem Ipsum is simply dummy text of the printing</div><div class="price" style="left:0;top:181px;font-size:12px">$199</div></div>
    <div class="card" style="left:500px;top:1953px;width:129px;height:220px"><div class="img" role="img" aria-label="Winter tyre product photo" style="height:140px"></div><div class="tyre" style="left:22px;top:26px;width:100px;height:108px"></div><span class="tag" style="left:9px;top:8px;font-size:5.5px">❄ Winter</span><div class="name" style="left:0;top:148px;width:129px;font-size:6.3px">Lorem Ipsum is simply dummy text of the printing</div><div class="price" style="left:0;top:181px;font-size:12px">$199</div></div>
    <div class="abs" style="left:74px;top:2196px;width:556px;height:1px;background:#3a3a3a"></div>
    <div class="btn btn-dark" style="left:290px;top:2220px;width:124px;height:25px;font-size:6.5px">View all Products →</div>

    <div class="photo" role="img" aria-label="Mechanic mounting a tyre with an impact wrench" style="left:0;top:2323px;width:704px;height:401px;background:linear-gradient(110deg,#1e1e1e 0%,#3d3d3d 35%,#6b6f73 60%,#2a2a2a 100%)"></div>
    <section class="abs" style="left:74px;top:2392px;width:320px;height:265px;background:linear-gradient(180deg,#f4f4f4,#cfcfcf)">
      <div class="h2 dark" style="left:34px;top:42px;font-size:19px">Our Tire Mounting<br>Service</div>
      <div class="rule" style="left:200px;top:53px;width:55px"></div>
      <p class="para dark" style="left:34px;top:94px;width:250px;font-size:6.3px">Lorem Ipsum is simply dummy text of the printing and typesetting industry. Lorem Ipsum has been the industry's standard dummy text ever since the 1500s, when an unknown printer took a galley of type and scrambled it to make a type specimen book.</p>
      <ul class="abs" style="left:48px;top:142px;font-size:6.3px;color:#333;line-height:1.5">
        <li>Lorem Ipsum is simply dummy text of the printing.</li>
        <li>Ipsum is simply dummy.</li>
        <li>printing and typesetting industry.</li>
        <li>Lorem Ipsum is simply dummy text</li>
      </ul>
      <div class="btn" style="left:34px;top:206px;width:135px;height:26px;font-size:6.5px">Mounting &amp; Repairs →</div>
    </section>

    <footer class="abs" style="left:0;top:2724px;width:704px;height:206px;background:var(--ink-2)">
      <div class="logo" style="left:74px;top:32px;font-size:18px">Velgrijder</div>
      <p class="para" style="left:74px;top:90px;width:175px;font-size:6px">Lorem Ipsum is simply dummy text of the printing and typesetting industry. Lorem Ipsum has been the industry's standard dummy text ever since the 1500s, when an unknown printer took a galley of type and scrambled it to make a type.</p>
      <div class="social" style="left:74px;top:155px;gap:6px"><span style="width:16px;height:16px;background:#3a5ba0"></span><span style="width:16px;height:16px;background:#d6356b"></span><span style="width:16px;height:16px;background:#1f7bbf"></span></div>
      <div class="abs" style="left:310px;top:30px;font-size:7px;font-weight:700;letter-spacing:1px">QUICK LINKS</div>
      <ul class="links" style="left:310px;top:50px;font-size:6.3px;line-height:2">
        <li>About us</li><li>Shop</li><li>Brands</li><li>Mounting &amp; Repairs</li><li>Team</li><li>Blogs</li><li>FAQs</li><li>Shipping &amp; Refund</li><li>Contact us</li>
      </ul>
      <div class="abs" style="left:430px;top:30px;font-size:7px;font-weight:700;letter-spacing:1px">NEWSLETTER SUBSCRIPTION</div>
      <p class="para" style="left:430px;top:52px;width:200px;font-size:6.3px">Lorem Ipsum is simply dummy text of the printing and typesetting industry.</p>
      <div class="input" style="left:430px;top:95px;width:200px;height:22px;font-size:6px;padding:0 8px">Enter Address<svg width="11" height="11" viewBox="0 0 12 12"><path d="M1 6l10-5-3 10-2-4z" fill="var(--red)"/></svg></div>
      <p class="para" style="left:430px;top:150px;width:200px;font-size:6px">© 2023 Velgrijder. All right reserved &nbsp;|&nbsp; Terms &amp; Conditions<br>| Privacy Policy</p>
    </footer>
  </main>

  <!-- MOBILE -->
  <aside class="abs mobile" style="left:921px;top:945px;width:183px;height:2923px;background:var(--ink);overflow:hidden">
    <div class="abs" style="left:0;top:0;width:183px;height:20px;background:var(--ink-3)"></div>
    <svg class="abs" style="left:9px;top:6px" width="8" height="8" viewBox="0 0 10 10"><circle cx="4" cy="4" r="3" fill="none" stroke="#ccc" stroke-width="1.3"/><path d="M6.5 6.5L9 9" stroke="#ccc" stroke-width="1.3"/></svg>
    <div class="btn btn-dark" style="left:46px;top:0;width:64px;height:20px;font-size:4.5px">Summer Tires →</div>
    <div class="btn" style="left:114px;top:0;width:69px;height:20px;font-size:4.5px">Winter Tires →</div>
    <div class="logo" style="left:9px;top:34px;font-size:11px">Velgrijder</div>
    <svg class="abs" style="left:162px;top:34px" width="11" height="10" viewBox="0 0 14 13"><path d="M1 2h2l2 7h7l1-5H4" fill="none" stroke="#fff" stroke-width="1.2"/><circle cx="6" cy="11" r="1" fill="#fff"/><circle cx="11" cy="11" r="1" fill="#fff"/><circle cx="12" cy="2" r="2" fill="var(--red)"/></svg>

    <div class="photo" role="img" aria-label="Blue car wheel on a snowy road" style="left:0;top:175px;width:183px;height:135px;background:linear-gradient(180deg,var(--ink) 0%,#2c5874 45%,#2a2f36 100%)"></div>
    <div class="eyebrow" style="left:9px;top:87px;font-size:7px;letter-spacing:4px">OUR</div>
    <div class="display" style="left:9px;top:98px;font-size:24px"><span class="r">Winter</span><br>Tires</div>
    <p class="para" style="left:9px;top:152px;width:165px;font-size:4.8px">Lorem Ipsum is simply dummy text of the printing and typesetting industry. Lorem Ipsum has been the industry's standard dummy text ever since the 1500s, when an unknown printer took a galley.</p>
    <div class="btn btn-dark" style="left:9px;top:200px;width:56px;height:15px;font-size:4.5px">Shop Tires →</div>

    <section class="abs" style="left:9px;top:320px;width:165px;height:320px;background:linear-gradient(180deg,#f4f4f4,#cfcfcf)">
      <div class="h2 dark" style="left:12px;top:16px;font-size:8.5px;font-weight:700">Find Wheels &amp; Tires That Fit</div>
      <p class="para dark" style="left:12px;top:34px;width:140px;font-size:4.8px">Lorem Ipsum is simply dummy text of the printing and typesetting industry. Lorem Ipsum has been the industry's standard dummy text ever since the 1500s, when an unknown printer took a galley.</p>
      <div class="flabel" style="left:12px;top:82px;font-size:4.5px">BY SIZE</div>
      <div class="select" style="left:12px;top:92px;width:141px;height:14px;font-size:4.5px;padding:0 5px">Width</div>
      <div class="select" style="left:12px;top:110px;width:141px;height:14px;font-size:4.5px;padding:0 5px">Height</div>
      <div class="select" style="left:12px;top:128px;width:141px;height:14px;font-size:4.5px;padding:0 5px">Inch</div>
      <div class="flabel" style="left:12px;top:152px;font-size:4.5px">BY VEHICLE</div>
      <div class="select" style="left:12px;top:162px;width:141px;height:14px;font-size:4.5px;padding:0 5px">Model</div>
      <div class="flabel" style="left:12px;top:188px;font-size:4.5px">BRAND</div>
      <div class="select" style="left:12px;top:198px;width:141px;height:14px;font-size:4.5px;padding:0 5px">Model</div>
      <div class="flabel" style="left:12px;top:222px;font-size:4.5px">TYPE</div>
      <div class="select" style="left:12px;top:232px;width:141px;height:14px;font-size:4.5px;padding:0 5px">Select</div>
      <div class="btn" style="left:12px;top:270px;width:141px;height:18px;font-size:5px">Search →</div>
    </section>
    <div class="abs" style="left:91px;top:642px;width:0;height:26px;border-left:1px dashed #666"></div>

    <div class="h2" style="left:9px;top:690px;font-size:10px">How Our Winter Tires<br>Work</div>
    <p class="para" style="left:9px;top:718px;width:165px;font-size:4.8px">Lorem Ipsum is simply dummy text of the printing and typesetting industry. Lorem Ipsum has been the industry's standard dummy text ever since the 1500s, when an unknown printer took a galley.</p>
    <ul class="bullets" style="left:9px;top:758px;width:165px;font-size:4.8px">
      <li style="gap:9px;margin-bottom:12px"><span class="ic" style="width:9px;height:9px"></span>Compound remains flexible in cold weather.</li>
      <li style="gap:9px;margin-bottom:12px"><span class="ic" style="width:9px;height:9px"></span>Tread designed for traction in ice, slush and snow.</li>
      <li style="gap:9px;margin-bottom:12px"><span class="ic" style="width:9px;height:9px"></span>More sipes give thousands of biting edge.</li>
      <li style="gap:9px"><span class="ic" style="width:9px;height:9px"></span>Stud holes</li>
    </ul>
    <div class="photo" role="img" aria-label="Close-up of a winter tyre tread" style="left:0;top:910px;width:183px;height:120px;background:radial-gradient(ellipse at 50% 40%,#5c5c5c 0,#333 50%,var(--ink) 85%)"></div>

    <section class="abs" style="left:0;top:1030px;width:183px;height:432px;background:var(--light)">
      <div class="h2 dark" style="left:9px;top:16px;font-size:10px">More About Our Winter<br>Tires</div>
      <p class="para dark" style="left:9px;top:44px;width:165px;font-size:4.8px">Lorem Ipsum is simply dummy text of the printing and typesetting industry. Lorem Ipsum has been the industry's standard dummy text ever since the 1500s, when an unknown printer took a galley of type and scrambled it to make a type specimen book. It has survived not only five centuries, but also the leap into electronic typesetting, remaining essentially unchanged. It was popularised in the 1960s with the release of Plintor sheets containing Lorem Ipsum passages, and more recently with desktop publishing software like Kerndale Layout including versions of Lorem Ipsum.</p>
      <p class="para dark" style="left:9px;top:166px;width:165px;font-size:4.8px">Lorem Ipsum is simply dummy text of the printing and typesetting industry.</p>
      <div class="btn" style="left:9px;top:196px;width:62px;height:16px;font-size:4.5px;background:#f08a76">Shop Tires →</div>
      <div class="photo" role="img" aria-label="Car wheel in snow" style="left:0;top:260px;width:183px;height:172px;background:linear-gradient(180deg,var(--light) 0%,#c9ced3 40%,#9aa0a6 100%)"></div>
    </section>

    <section class="abs" style="left:9px;top:1471px;width:165px;height:231px;background:linear-gradient(180deg,var(--red),var(--red-deep))">
      <div class="feature" style="left:22px;top:22px;gap:12px;font-size:5px"><span class="fi" style="width:24px;height:24px"><svg width="12" height="12" viewBox="0 0 16 16"><circle cx="8" cy="8" r="6" fill="none" stroke="#fff" stroke-width="1.5"/><circle cx="8" cy="8" r="2.5" fill="#fff"/></svg></span>State of the Art<br>Mounting</div>
      <div class="feature" style="left:22px;top:74px;gap:12px;font-size:5px"><span class="fi" style="width:24px;height:24px"><svg width="13" height="10" viewBox="0 0 18 14"><path d="M1 2h10v8H1zM11 5h4l2 3v2h-6" fill="none" stroke="#fff" stroke-width="1.3"/><circle cx="4" cy="11" r="1.6" fill="#fff"/><circle cx="14" cy="11" r="1.6" fill="#fff"/></svg></span>Fast and Hassle<br>free Shipping</div>
      <div class="feature" style="left:22px;top:126px;gap:12px;font-size:5px"><span class="fi" style="width:24px;height:24px"><svg width="12" height="12" viewBox="0 0 16 16"><circle cx="8" cy="7" r="5" fill="none" stroke="#fff" stroke-width="1.3"/><path d="M5.5 7l2 2 3-3.5" fill="none" stroke="#fff" stroke-width="1.2"/></svg></span>100% Guaranteed<br>Fitment</div>
      <div class="feature" style="left:22px;top:178px;gap:12px;font-size:5px"><span class="fi" style="width:24px;height:24px"><svg width="12" height="12" viewBox="0 0 16 16"><circle cx="8" cy="5" r="3.5" fill="#fff"/><path d="M2 15c0-4 3-6 6-6s6 2 6 6z" fill="#fff"/></svg></span>We're Tire<br>Experts</div>
    </section>

    <div class="display" style="left:0;top:1754px;width:183px;text-align:center;font-size:19px"><span class="r">Shop</span> Now</div>
    <p class="para" style="left:9px;top:1780px;width:165px;text-align:center;font-size:4.8px">Lorem Ipsum is simply dummy text of the printing and typesetting industry. Lorem Ipsum has been the industry's standard dummy text ever since the 1500s, when an unknown printer took a galley.</p>
    <div class="card" style="left:26px;top:1838px;width:132px;height:200px"><div class="img" role="img" aria-label="Winter tyre product photo" style="height:160px"></div><div class="tyre" style="left:20px;top:34px;width:100px;height:116px"></div><span class="tag" style="left:9px;top:8px;font-size:4.5px">❄ Winter</span><div class="name" style="left:0;top:166px;width:132px;font-size:4.8px">Lorem Ipsum is simply dummy text of the printing</div><div class="price" style="left:0;top:186px;font-size:9px">$199</div></div>
    <svg class="abs" style="left:8px;top:1911px" width="6" height="10" viewBox="0 0 6 10"><path d="M5 1L1 5l4 4" fill="none" stroke="#888"/></svg>
    <svg class="abs" style="left:169px;top:1911px" width="6" height="10" viewBox="0 0 6 10"><path d="M1 1l4 4-4 4" fill="none" stroke="#888"/></svg>
    <div class="btn btn-dark" style="left:9px;top:2078px;width:165px;height:22px;font-size:4.8px">View all Products →</div>

    <section class="abs" style="left:0;top:2142px;width:183px;height:254px;background:linear-gradient(180deg,#f4f4f4,#cfcfcf)">
      <div class="h2 dark" style="left:9px;top:26px;font-size:10px">Our Tire Mounting<br>Service</div>
      <p class="para dark" style="left:9px;top:56px;width:165px;font-size:4.8px">Lorem Ipsum is simply dummy text of the printing and typesetting industry. Lorem Ipsum has been the industry's standard dummy text ever since the 1500s, when an unknown printer took a galley of type and scrambled it to make a type specimen book.</p>
      <ul class="abs" style="left:20px;top:106px;font-size:4.8px;color:#333;line-height:1.5">
        <li>Lorem Ipsum is simply dummy text of the printing.</li>
        <li>Ipsum is simply dummy.</li>
        <li>printing and typesetting industry.</li>
        <li>Lorem Ipsum is simply dummy text</li>
      </ul>
      <div class="btn" style="left:9px;top:163px;width:107px;height:20px;font-size:4.8px">Mounting &amp; Repairs →</div>
    </section>
    <div class="photo" role="img" aria-label="Mechanic mounting a tyre" style="left:0;top:2396px;width:183px;height:138px;background:linear-gradient(110deg,#2a2a2a 0%,#5e6266 50%,#2a2a2a 100%)"></div>

    <footer class="abs" style="left:0;top:2534px;width:183px;height:389px;background:var(--ink-2)">
      <div class="logo" style="left:0;top:30px;width:183px;text-align:center;font-size:11px">Velgrijder</div>
      <p class="para" style="left:9px;top:58px;width:165px;text-align:center;font-size:4.8px">Lorem Ipsum is simply dummy text of the printing and typesetting industry. Lorem Ipsum has been the industry's standard dummy text ever since the 1500s, when an unknown printer took a galley of type and scrambled it to make a type.</p>
      <div class="abs" style="left:0;top:122px;width:183px;text-align:center;font-size:5.5px;font-weight:700;letter-spacing:1px">QUICK LINKS</div>
      <ul class="links" style="left:0;top:136px;width:183px;text-align:center;font-size:4.8px;line-height:1.9">
        <li>About us</li><li>Shop</li><li>Brands</li><li>Mounting &amp; Repairs</li><li>Team</li><li>Blogs</li><li>FAQs</li><li>Shipping &amp; Refund</li><li>Contact us</li>
      </ul>
      <div class="abs" style="left:0;top:250px;width:183px;text-align:center;font-size:5.5px;font-weight:700;letter-spacing:1px">NEWSLETTER SUBSCRIPTION</div>
      <p class="para" style="left:9px;top:264px;width:165px;text-align:center;font-size:4.8px">Lorem Ipsum is simply dummy text of the printing and typesetting industry.</p>
      <div class="input" style="left:9px;top:291px;width:165px;height:17px;font-size:4.5px;padding:0 6px">Enter Address<svg width="9" height="9" viewBox="0 0 12 12"><path d="M1 6l10-5-3 10-2-4z" fill="var(--red)"/></svg></div>
      <p class="para" style="left:9px;top:320px;width:165px;text-align:center;font-size:4.5px">© 2023 Velgrijder. All right reserved &nbsp;|&nbsp; Terms &amp; Conditions &nbsp;|&nbsp; Privacy Policy</p>
      <div class="social" style="left:71px;top:345px;gap:5px"><span style="width:13px;height:13px;background:#3a5ba0"></span><span style="width:13px;height:13px;background:#d6356b"></span><span style="width:13px;height:13px;background:#1f7bbf"></span></div>
    </footer>
  </aside>

</div>
</body>
</html>
```